RevelHubQZ Business Cards

Front
Has logo with a design. Website address (www.revelhubqz.example)
Has slogan (discover nightlife)
Has phone number (5129873304)
Should be bold and stands out.

Back
Has details about what we offer.

Events
Search upcoming events
Submit events
Party Image Gallery
View and download HQ party images
Sign up as a contributing event photographer and get paid!
Tickets
Sell your event tickets online for free!
Direct pay
No ticket fee

Target Market(s)

These cards will be handed out in clubs and events to patrons.

Industry/Entity Type

Business

Contact Information for Business Card

Should match or mirror our website in some sort of way. Visit the website to get ideas.

Requirements
Must have
• Must be designed for a 3x3 inch card.

```html
<!DOCTYPE html>
<html lang="en">
<head>
<meta charset="utf-8">
<title>RevelHubQZ Business Cards</title>
<link rel="stylesheet" href="https://fonts.googleapis.com/css2?family=Varela+Round&display=swap">
<style>
  :root {
    --stage: #3b3531;
    --card: #0b0b0b;
    --card-edge: #1a1a1a;
    --brand-blue: #3aa8de;
    --brand-pink: #e8409a;
    --slogan-grey: #9a9a9a;
    --body-grey: #c4c4c4;
    --silver: #cfcfcf;
  }
  * { margin: 0; padding: 0; box-sizing: border-box; }
  html, body {
    width: 1200px;
    height: 900px;
    overflow: hidden;
    background: var(--stage);
    font-family: "Varela Round", Arial, sans-serif;
  }
  .sheet {
    width: 1200px;
    height: 900px;
    display: flex;
    align-items: center;
    justify-content: center;
    gap: 60px;
  }
  .card {
    width: 480px;
    height: 480px;
    background: var(--card);
    border: 1px solid var(--card-edge);
    border-radius: 4px;
    box-shadow: 0 14px 30px rgba(0, 0, 0, 0.45);
    display: flex;
    flex-direction: column;
  }

  /* Front */
  .card--front {
    align-items: center;
    justify-content: center;
  }
  .brand {
    display: flex;
    align-items: center;
    gap: 14px;
  }
  .brand__dot {
    width: 46px;
    height: 46px;
    border-radius: 50%;
    background: var(--brand-pink);
    flex: none;
  }
  .brand__name {
    font-size: 44px;
    line-height: 1;
    color: var(--brand-blue);
    letter-spacing: 0.5px;
  }
  .slogan {
    margin-top: 12px;
    margin-left: 60px;
    font-size: 15px;
    letter-spacing: 5px;
    color: var(--slogan-grey);
  }
  .contact {
    margin-top: 48px;
    text-align: center;
  }
  .contact__phone {
    display: inline-flex;
    align-items: center;
    gap: 10px;
    font-size: 26px;
    color: var(--brand-blue);
  }
  .contact__phone svg { width: 20px; height: 20px; }
  .contact__web {
    margin-top: 16px;
    font-size: 20px;
    letter-spacing: 0.5px;
    color: var(--brand-pink);
  }

  /* Back */
  .card--back {
    padding: 40px 44px;
  }
  .card--back .brand { gap: 10px; }
  .card--back .brand__dot { width: 26px; height: 26px; background: var(--silver); }
  .card--back .brand__name { font-size: 26px; color: var(--silver); }
  .offers {
    margin-top: 26px;
    list-style: none;
    display: flex;
    flex-direction: column;
    gap: 20px;
  }
  .offer__title {
    font-size: 20px;
    color: var(--brand-blue);
    margin-bottom: 6px;
  }
  .offer:nth-child(2) .offer__title { color: var(--brand-pink); }
  .offer__items {
    list-style: none;
  }
  .offer__items li {
    position: relative;
    padding-left: 16px;
    font-size: 14px;
    line-height: 1.55;
    color: var(--body-grey);
  }
  .offer__items li::before {
    content: "";
    position: absolute;
    left: 0;
    top: 8px;
    width: 6px;
    height: 6px;
    border-radius: 50%;
    background: var(--brand-pink);
  }
</style>
</head>
<body>
<main class="sheet">
  <section class="card card--front" aria-label="Card front">
    <div class="brand-block">
      <div class="brand">
        <span class="brand__dot"></span>
        <span class="brand__name">RevelHubQZ</span>
      </div>
      <p class="slogan">discover nightlife</p>
    </div>
    <div class="contact">
      <p class="contact__phone">
        <svg viewBox="0 0 24 24" aria-hidden="true"><path fill="#e8409a" d="M6.6 10.8a15.1 15.1 0 0 0 6.6 6.6l2.2-2.2c.3-.3.7-.4 1-.2 1.1.4 2.3.6 3.6.6.6 0 1 .4 1 1V20c0 .6-.4 1-1 1C10.6 21 3 13.4 3 4c0-.6.4-1 1-1h3.5c.6 0 1 .4 1 1 0 1.3.2 2.5.6 3.6.1.3 0 .7-.2 1z"/></svg>
        5129873304
      </p>
      <p class="contact__web">www.revelhubqz.example</p>
    </div>
  </section>

  <section class="card card--back" aria-label="Card back">
    <div class="brand">
      <span class="brand__dot"></span>
      <span class="brand__name">RevelHubQZ</span>
    </div>
    <ul class="offers">
      <li class="offer">
        <h2 class="offer__title">Events</h2>
        <ul class="offer__items">
          <li>Search upcoming events</li>
          <li>Submit events</li>
        </ul>
      </li>
      <li class="offer">
        <h2 class="offer__title">Party Image Gallery</h2>
        <ul class="offer__items">
          <li>View and download HQ party images</li>
          <li>Sign up as a contributing event photographer and get paid!</li>
        </ul>
      </li>
      <li class="offer">
        <h2 class="offer__title">Tickets</h2>
        <ul class="offer__items">
          <li>Sell your event tickets online for free!</li>
          <li>Direct pay</li>
          <li>No ticket fee</li>
        </ul>
      </li>
    </ul>
  </section>
</main>
</body>
</html>
```